Herbal tea retail bag needs a label sticker

Hi Derek
I want to change my present packaging (see photo), I wish to have more colorful label as old label is small and 3 color only. The size will be 6 cm x 9 cm.

The herbal tea such as roses, chamomile, peppermint leaves, Detox blend etc, I have wide range of products, inclusive single tea and tea blends, they will using same label. The teas are natural plants, they are beautiful and healthy. Therefore, I wish to have a very natural and bright design. I need blank places for me to input product name, company info (logo, address) , weight, description, expiry date, disclaimer , how to drink. etc

Thank you.
Mabel

Target Market(s)

End user who appreciate herbal tea drink and love the natural herbs.

Industry/Entity Type

Food Store

Requirements
Must have
• Clear pictures of herbal tea are a healthy drink, nature and safe.
• Blank places for us to input products information, company information and general information.
Nice to have
• We like to see using natures plants, leaves or flower as design material.
Should not have
• Should not have modern graphic, technical of graphic.

```html
<!DOCTYPE html>
<html lang="en">
<head>
<meta charset="utf-8">
<title>Herbal Tea Label – Peppermint</title>
<link rel="stylesheet" href="https://fonts.googleapis.com/css2?family=Fira+Sans:ital,wght@0,400;0,600;1,400&family=Libre+Caslon+Text&display=swap">
<style>
  :root {
    --page: #ffffff;
    --ink: #222222;
    --label-top: #ffffff;
    --label-bottom: #ece9ea;
    --label-edge: #8c8c8c;
    --title: #d46a52;
    --body: #d9785c;
    --gold: #d1913a;
    --icon: #b6bd38;
    --petal-green: rgba(120, 150, 40, 0.75);
    --petal-orange: rgba(240, 130, 40, 0.8);
    --petal-yellow: rgba(248, 205, 110, 0.55);
  }
  * { box-sizing: border-box; margin: 0; padding: 0; }
  html, body { width: 1200px; height: 1000px; overflow: hidden; background: var(--page); }
  body { position: relative; font-family: "Fira Sans", sans-serif; color: var(--ink); }

  .label {
    position: absolute;
    width: 426px; height: 298px;
    background: linear-gradient(160deg, var(--label-top) 30%, var(--label-bottom) 100%);
    border: 1px solid var(--label-edge);
    overflow: hidden;
    transform-origin: 0 0;
  }
  .label--small { transform: scale(0.6667); }
  .label--blank-a { left: 58px; top: 144px; }
  .label--blank-b { left: 58px; top: 370px; }
  .label--filled { left: 58px; top: 596px; }
  .label--enlarged { left: 612px; top: 224px; border-color: #d8d2c4; }

  .label__petals {
    position: absolute; left: 160px; top: -10px; width: 280px; height: 320px;
    background:
      radial-gradient(ellipse 55% 25% at 25% 6%, var(--petal-green), transparent 70%),
      radial-gradient(ellipse 30% 45% at 62% 22%, var(--petal-orange), transparent 75%),
      radial-gradient(ellipse 45% 70% at 60% 55%, var(--petal-yellow), transparent 75%),
      radial-gradient(ellipse 40% 40% at 15% 40%, rgba(190, 200, 120, 0.35), transparent 75%);
  }

  .label__origin {
    position: absolute; right: 10px; top: 8px;
    font-size: 10px; font-weight: 600; color: #b8563e;
  }
  .label__title {
    position: absolute; left: 18px; top: 30px;
    font-family: "Libre Caslon Text", serif; font-weight: 400;
    font-size: 34px; letter-spacing: 0.5px; color: var(--title);
  }
  .label__uses {
    position: absolute; left: 18px; top: 78px; width: 400px;
    font-size: 12.4px; font-weight: 600; line-height: 16px; color: var(--body);
  }
  .label__method {
    position: absolute; left: 18px; top: 130px; width: 380px;
    font-size: 12.4px; font-style: italic; line-height: 16px; color: var(--body);
  }
  .label__notes {
    position: absolute; left: 228px; top: 182px;
    font-size: 11.5px; font-weight: 600; line-height: 16px; color: var(--gold);
  }
  .label__weight {
    position: absolute; left: 228px; top: 218px;
    font-size: 16px; font-weight: 600; color: var(--title);
  }
  .label__expiry {
    position: absolute; left: 228px; top: 239px;
    font-size: 12px; color: var(--gold);
  }
  .label__web {
    position: absolute; left: 228px; top: 266px;
    font-size: 11.5px; font-weight: 600; color: var(--title);
  }

  .label__icons {
    position: absolute; left: 385px; top: 220px;
    display: flex; flex-direction: column; gap: 7px;
  }
  .label__icons svg { width: 16px; height: 16px; display: block; }

  .caption { position: absolute; font-size: 13px; color: var(--ink); }
  .caption--size { left: 58px; top: 820px; }
  .caption--scale { left: 594px; top: 960px; font-size: 12px; }
</style>
</head>
<body>

<svg width="0" height="0" style="position:absolute">
  <defs>
    <g id="icon-leaf"><circle cx="8" cy="8" r="7.5" fill="var(--icon)"/><path d="M4.5 10.5 C5 6 8 4.5 11.5 4.5 C11.5 8 9.5 11 4.5 10.5 Z" fill="#fff"/></g>
    <g id="icon-tick"><circle cx="8" cy="8" r="7.5" fill="var(--icon)"/><path d="M4.5 8.2 L7 10.5 L11.5 5.5" stroke="#fff" stroke-width="1.8" fill="none"/></g>
    <g id="icon-cycle"><circle cx="8" cy="8" r="7.5" fill="var(--icon)"/><circle cx="8" cy="8" r="3.4" stroke="#fff" stroke-width="1.6" fill="none"/></g>
  </defs>
</svg>

<div class="label label--small label--blank-a">
  <div class="label__petals" role="img" aria-label="Fanned leaves and flower petals in green, orange and pale yellow"></div>
  <div class="label__icons">
    <svg viewBox="0 0 16 16"><use href="#icon-leaf"/></svg>
    <svg viewBox="0 0 16 16"><use href="#icon-tick"/></svg>
    <svg viewBox="0 0 16 16"><use href="#icon-cycle"/></svg>
  </div>
</div>

<div class="label label--small label--blank-b">
  <div class="label__petals" role="img" aria-label="Fanned leaves and flower petals in green, orange and pale yellow"></div>
  <div class="label__icons">
    <svg viewBox="0 0 16 16"><use href="#icon-leaf"/></svg>
    <svg viewBox="0 0 16 16"><use href="#icon-tick"/></svg>
    <svg viewBox="0 0 16 16"><use href="#icon-cycle"/></svg>
  </div>
</div>

<div class="label label--small label--filled">
  <div class="label__petals" role="img" aria-label="Fanned leaves and flower petals in green, orange and pale yellow"></div>
  <p class="label__origin">Origin: Mediterranean</p>
  <h2 class="label__title">PEPPERMINT</h2>
  <p class="label__uses">For depression, anxiety, lethargy, weakness, female discomfort, aches and pains, poor circulation, muscle pains, normalises complexion, improves youthfulness and beauty</p>
  <p class="label__method">Infuse 1 teaspoonful of tea with hot boiling water, allow to steep for 3-5 minutes before serving</p>
  <p class="label__notes">Suitable for Vegans.<br>Store in a cool and dry place.</p>
  <p class="label__weight">Net wt. 60g</p>
  <p class="label__expiry">Best before Dec 2018</p>
  <p class="label__web">leafwell-tea.com</p>
  <div class="label__icons">
    <svg viewBox="0 0 16 16"><use href="#icon-leaf"/></svg>
    <svg viewBox="0 0 16 16"><use href="#icon-tick"/></svg>
    <svg viewBox="0 0 16 16"><use href="#icon-cycle"/></svg>
  </div>
</div>

<p class="caption caption--size">Actual 7cm x 10cm</p>

<div class="label label--enlarged">
  <div class="label__petals" role="img" aria-label="Fanned leaves and flower petals in green, orange and pale yellow"></div>
  <p class="label__origin">Origin: Mediterranean</p>
  <h1 class="label__title">PEPPERMINT</h1>
  <p class="label__uses">For depression, anxiety, lethargy, weakness, female discomfort, aches and pains, poor circulation, muscle pains, normalises complexion, improves youthfulness and beauty</p>
  <p class="label__method">Infuse 1 teaspoonful of tea with hot boiling water, allow to steep for 3-5 minutes before serving</p>
  <p class="label__notes">Suitable for Vegans.<br>Store in a cool and dry place.</p>
  <p class="label__weight">Net wt. 60g</p>
  <p class="label__expiry">Best before Dec 2018</p>
  <p class="label__web">leafwell-tea.com</p>
  <div class="label__icons">
    <svg viewBox="0 0 16 16"><use href="#icon-leaf"/></svg>
    <svg viewBox="0 0 16 16"><use href="#icon-tick"/></svg>
    <svg viewBox="0 0 16 16"><use href="#icon-cycle"/></svg>
  </div>
</div>

<p class="caption caption--scale">150%</p>

</body>
</html>
```